meridale partners business card

Architectural firm business card
Updates

Please note:

corporate colour black+yellow are the only elements to be kept.
NO OTHER ELEMENT TO BE REUSED FROM PREVIOUS BUSINESS CARD.
Thank you.

Dear Everyone,

Thank you for your participation. I have upload the KBSO+ logo again for incoporate in the card. in tif and pdf format.

Thank you 

I keep getting request for the logo file. Does everyone has the same problem?

I cannot do much, because the file is upload to the website server. I can't seem to see it either.

The logo file is now working. Please download. I check it myself. Thank you everyone.

Dear All,

Thank you for all the hard work. There are a lot of great work. Due to current commitment with work, I am unable to review them just yet. I will do so next week and advise everyone also. Thank you again. Best regards

Dear All,

Thank you for your participation. There are a lot of good design. Unfortunately, I can only select one. All the best. This is definitely a good crowd to work with. Thank you everyone again.

Best regards

Target Market(s)

Corporate, commercial and institutional projects only

Industry/Entity Type

Business

Requirements
Must have
• elegant simple
double sided with coating
Member of Southland Guild of Draughtsmen (logo only)
corporate colour black and

LOGO FILE UPLOADED
Should not have
• should not be the same as current business card.
upload for reference information only.
font sans serif preferred.

```html
<!DOCTYPE html>
<html lang="en">
<head>
<meta charset="utf-8">
<title>meridale partners business card</title>
<link href="https://fonts.googleapis.com/css2?family=Exo+2:wght@400;600;800&display=swap" rel="stylesheet">
<style>
  :root {
    --orange: #f7962f;
    --black: #0b0b0b;
    --ink: #111111;
    --muted: #8a8a8a;
    --ghost: #1c1c1c;
    --stage: #d9d9d9;
  }
  * { box-sizing: border-box; margin: 0; padding: 0; }
  html, body { width: 1200px; height: 900px; overflow: hidden; }
  body {
    background: var(--stage);
    font-family: "Exo 2", Arial, sans-serif;
    position: relative;
  }
  .card {
    position: absolute;
    border-radius: 18px;
    overflow: hidden;
  }

  /* front */
  .card-front {
    left: 110px; top: 170px;
    width: 340px; height: 560px;
    background: var(--orange);
    color: var(--ink);
  }
  .front-name {
    position: absolute;
    right: 28px; top: 50px;
    text-align: right;
    font-weight: 800;
    font-size: 66px;
    line-height: 0.88;
    letter-spacing: -1px;
  }
  .front-tab {
    position: absolute;
    left: 0; top: 318px;
    width: 26px; height: 58px;
    background: var(--black);
  }
  .services {
    position: absolute;
    left: 48px; top: 316px;
    list-style: none;
    font-size: 15px;
    line-height: 1.28;
  }
  .services li::before { content: "| "; }
  .front-web {
    position: absolute;
    left: 48px; top: 400px;
    font-size: 16px;
    font-weight: 600;
  }

  /* back */
  .card-back {
    left: 520px; top: 280px;
    width: 580px; height: 340px;
    background: var(--black);
    color: var(--muted);
  }
  .back-ghost {
    position: absolute;
    right: -10px; top: 14px;
    font-weight: 800;
    font-size: 118px;
    line-height: 0.9;
    text-align: right;
    color: var(--ghost);
    letter-spacing: -2px;
  }
  .back-name {
    position: absolute;
    left: 46px; top: 110px;
    font-weight: 800;
    font-size: 30px;
    color: var(--orange);
    letter-spacing: -0.5px;
  }
  .back-tab {
    position: absolute;
    left: 0; top: 176px;
    width: 30px; height: 74px;
    background: var(--orange);
  }
  .person {
    position: absolute;
    left: 46px; top: 172px;
    font-size: 12px;
    line-height: 1.3;
  }
  .person .full-name { color: var(--orange); font-size: 18px; font-weight: 600; }
  .person .creds { font-size: 11px; }
  .contact {
    position: absolute;
    left: 46px; top: 240px;
    font-size: 11.5px;
    line-height: 1.35;
  }
  .contact b { color: var(--orange); font-weight: 600; }
</style>
</head>
<body>

<section class="card card-front" aria-label="Card front">
  <div class="front-name">meridale<br>partners</div>
  <div class="front-tab"></div>
  <ul class="services">
    <li>architects</li>
    <li>urban planners</li>
    <li>project managers</li>
  </ul>
  <div class="front-web">www.meridalepartners.com.au</div>
</section>

<section class="card card-back" aria-label="Card back">
  <div class="back-ghost" aria-hidden="true">meridale<br>partners</div>
  <div class="back-name">meridale partners</div>
  <div class="back-tab"></div>
  <div class="person">
    <div class="full-name">Lena Hartwell <span class="creds">kbso</span></div>
    <div>Architect (reg no 4172)</div>
    <div>Director</div>
  </div>
  <div class="contact">
    <div>Alder House</div>
    <div>14 Kestrel Lane, Northvale 4821</div>
    <div><b>Mob:</b> 0400 118 274 <b>Tel:</b> + 00 5550 1234 <b>Fax:</b> + 00 5550 1299</div>
    <div><b>Email:</b> mail@meridalepartners.com.au</div>
    <div><b>Web:</b> www.meridalepartners.com.au</div>
  </div>
</section>

</body>
</html>
```